Stridewell Specialists Stationary

At Stridewell Specs, we know that rehab technology is much more than a tool or machine. It’s mobility for your body and productivity and freedom for your lifestyle to reclaim your life. That’s why we specialize in custom power and manual wheelchairs, scooters, complex seating and positioning, standers, and bathroom equipment that all help you reclaim your life.

Our rehab equipment includes custom power wheelchairs offering complex, customized seating and positioning systems with an array of specialized electronic control features. With a certified staff of Assistive Technology Professionals (ATPs) and technical repair department, we provide knowledgeable assistance to make sure you get the right products needed to reclaim your life – delivered on time, right to your door.

```html
<!DOCTYPE html>
<html lang="en">
<head>
<meta charset="utf-8">
<title>Stridewell Specialists Stationery</title>
<link href="https://fonts.googleapis.com/css2?family=Oxygen:wght@400;700&display=swap" rel="stylesheet">
<style>
  :root {
    --navy: #0f3257;
    --green: #8cc63f;
    --paper: #ffffff;
    --ink: #3a3a3a;
    --backdrop: #e9eaec;
  }
  * { box-sizing: border-box; margin: 0; padding: 0; }
  html, body { width: 1200px; height: 937px; overflow: hidden; }
  body { background: var(--backdrop); font-family: "Oxygen", Arial, sans-serif; position: relative; }
  .sheet { position: absolute; background: var(--paper); overflow: hidden; }
  .sheet svg.shape { position: absolute; left: 0; top: 0; }

  .brand { position: absolute; color: var(--navy); font-weight: 700; line-height: 1; white-space: nowrap; }
  .brand .name { display: block; }
  .brand .sub { display: block; letter-spacing: .28em; }
  .brand .dot { display: inline-block; border-radius: 50%; background: var(--navy); vertical-align: middle; }

  /* Letterhead */
  .letterhead { left: 185px; top: 68px; width: 388px; height: 544px; }
  .letterhead .brand { left: 42px; top: 34px; }
  .letterhead .brand .name { font-size: 24px; }
  .letterhead .brand .sub { font-size: 7.5px; margin-top: 3px; }
  .letter { position: absolute; left: 36px; top: 136px; width: 300px; font-size: 5.4px; line-height: 7.6px; color: var(--ink); }
  .letter p { margin-bottom: 7px; }
  .letter .gap { margin-bottom: 16px; }
  .signature { width: 22px; height: 16px; background: linear-gradient(90deg, #cfcfcf, #e6e6e6); margin: 4px 0 4px; }
  .letter .signer { font-weight: 700; }
  .contacts { position: absolute; right: 20px; list-style: none; text-align: right; color: #fff; font-size: 5.4px; line-height: 9.4px; }
  .contacts li::after { content: ""; display: inline-block; width: 6px; height: 6px; border-radius: 50%; background: #fff; margin-left: 4px; vertical-align: -1px; }
  .letterhead .contacts { top: 467px; }

  /* Folder */
  .folder { left: 636px; top: 41px; width: 458px; height: 575px; background: var(--navy); }
  .folder .brand { left: 0; right: 0; top: 264px; text-align: center; }
  .folder .brand .name { font-size: 50px; }
  .folder .brand .sub { font-size: 15px; margin-top: 6px; letter-spacing: .3em; }
  .site { position: absolute; left: 0; right: 0; text-align: center; color: #fff; letter-spacing: .2em; }
  .folder .site { top: 552px; font-size: 11.5px; }

  /* Business cards */
  .card { left: 45px; width: 177px; height: 99px; border-radius: 8px; }
  .card-front { top: 658px; }
  .card-back { top: 785px; }
  .card-front .brand { left: 0; right: 0; top: 13px; text-align: center; }
  .card-front .brand .name { font-size: 13px; }
  .card-front .brand .sub { font-size: 4.5px; margin-top: 1px; }
  .card-back .brand { left: 0; right: 0; top: 34px; text-align: center; }
  .card-back .brand .name { font-size: 18px; }
  .card-back .brand .sub { font-size: 5.5px; margin-top: 2px; }
  .holder { position: absolute; left: 16px; top: 54px; color: #fff; font-size: 5.4px; line-height: 7px; }
  .holder strong { letter-spacing: .04em; }
  .divider { position: absolute; left: 102px; top: 50px; width: 1px; height: 30px; background: rgba(255,255,255,.7); }
  .card-front .contacts { left: 106px; right: auto; top: 48px; text-align: left; font-size: 3.8px; line-height: 6px; }
  .card-front .contacts li::after { display: none; }
  .card-front .contacts li::before { content: ""; display: inline-block; width: 3.5px; height: 3.5px; border-radius: 50%; background: #fff; margin-right: 3px; vertical-align: -.5px; }

  /* Envelopes */
  .envelope { top: 671px; width: 439px; height: 209px; }
  .envelope-front { left: 265px; }
  .envelope-front .brand { left: 16px; top: 30px; }
  .envelope-front .brand .name { font-size: 23px; }
  .envelope-front .brand .sub { font-size: 7px; margin-top: 3px; }
  .envelope-front .site { top: 155px; font-size: 10px; }
  .envelope-back { left: 737px; }
  .envelope-back .site { top: 30px; font-size: 11px; }
</style>
</head>
<body>

<section class="sheet letterhead">
  <svg class="shape" width="388" height="544" viewBox="0 0 388 544">
    <path d="M0 448 Q194 470 388 448 L388 544 L0 544 Z" fill="var(--navy)"/>
    <path d="M0 446 Q194 468 388 446" fill="none" stroke="var(--green)" stroke-width="2.5"/>
  </svg>
  <div class="brand"><span class="name">Stridewell</span><span class="sub">SPECIALISTS</span></div>
  <div class="letter">
    <p>July 2, 2012</p>
    <p><strong>Dear Client,</strong><br>12 Birch Lane, Harbor St., Country Name</p>
    <p class="gap">We are pleased to share our updated range of custom power and manual wheelchairs, scooters, complex seating and positioning systems, standers and bathroom equipment. Our certified team of assistive technology professionals is ready to assess your needs and guide you to the right products, delivered on time and right to your door, so you can move freely every day.</p>
    <p class="gap">Our technical repair department keeps every chair running smoothly, with quick service visits and clear advice whenever you need it.</p>
    <p class="gap">Each custom power wheelchair we fit offers tailored seating and positioning along with a wide array of specialized electronic controls. We take the time to learn how you live, work and travel, then build a setup that supports your body and your goals. Call us to book a free home consultation with our friendly specialists today.</p>
    <p>Best Regards,</p>
    <div class="signature" role="img" aria-label="Handwritten signature"></div>
    <p><span class="signer">Daniel Reyes</span><br>Director<br><br>12 Birch Lane, Harbor St., Country Name</p>
  </div>
  <ul class="contacts">
    <li>555 014 2290</li>
    <li>555 014 2291</li>
    <li>hello@stridewellspecs.com</li>
    <li>www.stridewellspecs.com</li>
    <li>48 Meadow Park Road, Suite 3</li>
  </ul>
</section>

<section class="sheet folder">
  <svg class="shape" width="458" height="575" viewBox="0 0 458 575">
    <path d="M0 203 Q229 256 458 203 L458 373 Q229 330 0 373 Z" fill="#f4f4f4"/>
    <path d="M0 203 Q229 256 458 203" fill="none" stroke="var(--green)" stroke-width="3"/>
    <path d="M0 373 Q229 330 458 373" fill="none" stroke="var(--green)" stroke-width="3"/>
  </svg>
  <div class="brand"><span class="name">Stridewell</span><span class="sub">SPECIALISTS</span></div>
  <p class="site">www.stridewellspecs.com</p>
</section>

<section class="sheet card card-front">
  <svg class="shape" width="177" height="99" viewBox="0 0 177 99">
    <path d="M0 38 Q88 48 177 38 L177 90 Q88 80 0 90 Z" fill="var(--navy)"/>
    <path d="M0 37 Q88 47 177 37" fill="none" stroke="var(--green)" stroke-width="1.5"/>
    <path d="M0 91 Q88 81 177 91" fill="none" stroke="var(--green)" stroke-width="1.5"/>
  </svg>
  <div class="brand"><span class="name">Stridewell</span><span class="sub">SPECIALISTS</span></div>
  <p class="holder"><strong>MARCUS HALE</strong><br>Managing Director</p>
  <span class="divider"></span>
  <ul class="contacts">
    <li>555 014 2290</li>
    <li>555 014 2291</li>
    <li>hello@stridewellspecs.com</li>
    <li>www.stridewellspecs.com</li>
    <li>48 Meadow Park Road, Suite 3</li>
  </ul>
</section>

<section class="sheet card card-back">
  <div class="brand"><span class="name">Stridewell</span><span class="sub">SPECIALISTS</span></div>
</section>

<section class="sheet envelope envelope-front">
  <svg class="shape" width="439" height="209" viewBox="0 0 439 209">
    <path d="M0 128 Q219 138 439 128 L439 178 Q219 168 0 178 Z" fill="var(--navy)"/>
    <path d="M0 127 Q219 137 439 127" fill="none" stroke="var(--green)" stroke-width="2"/>
    <path d="M0 179 Q219 169 439 179" fill="none" stroke="var(--green)" stroke-width="2"/>
  </svg>
  <div class="brand"><span class="name">Stridewell</span><span class="sub">SPECIALISTS</span></div>
  <p class="site">www.stridewellspecs.com</p>
</section>

<section class="sheet envelope envelope-back">
  <svg class="shape" width="439" height="209" viewBox="0 0 439 209">
    <path d="M0 0 H439 V38 Q439 71 406 71 H33 Q0 71 0 38 Z" fill="var(--navy)"/>
  </svg>
  <p class="site">www.stridewellspecs.com</p>
</section>

</body>
</html>
```